Business Card Design

Bramwell Pantry is the name of my health coaching business. My tag line is "Where good health meets real life." I will be working with clients one-on-one and in groups. My target clients are women "of a certain age" who want to be more comfortable in their own skin. We will work together in a 6-month program. The coaching sessions will take place in my kitchen. I will also be conducting monthly cooking classes and field trips - to farmer's markets, speciality markets etc.. for my clients.
Updates

the business name is Bramwell Pantry - I'm not sure how the p got in there at the end of the name

Thank you

Please include the website - www.bramwellpantry-example.com and the tag line:

Where good health meets real life on the business card.

Thank you

Please add the phone number to the business card - sorry, I forgot to state that in the original brief

(555) 218-4476

Target Market(s)

Women "of a certain age" who want to be more comfortable in their own skin

Industry/Entity Type

Cooking

Contact Information for Business Card

Bramwell Pantry
Where good health meets real life

Harriet Dunmore
Health Coach
(555) 218-4476

Font styles to use
Serif
Sans Serif

Requirements
Must have
• front & back design
I typical like soft colors - and have tended toward greens over time - I'm open although I would not like bright reds, yellows etc..

```html
<!DOCTYPE html>
<html lang="en">
<head>
<meta charset="utf-8">
<title>Bramwell Pantry – Business Card</title>
<link rel="stylesheet" href="https://fonts.googleapis.com/css2?family=Fjalla+One&family=Libre+Baskerville:ital,wght@0,700;1,700&family=Arimo:ital,wght@0,400;0,700;1,700&display=swap">
<style>
  :root {
    --backdrop: #d9dcda;
    --card-green: #74c3a1;
    --card-green-deep: #67b693;
    --ink-teal: #1f3b3c;
    --ink-slate: #2b4a4c;
    --ink-black: #111a1a;
  }
  * { box-sizing: border-box; margin: 0; padding: 0; }
  html, body {
    width: 1200px;
    height: 900px;
    overflow: hidden;
    background: var(--backdrop);
  }
  .canvas {
    position: relative;
    width: 1200px;
    height: 900px;
    display: flex;
    flex-direction: column;
    align-items: center;
    justify-content: center;
    gap: 50px;
  }
  .card {
    width: 620px;
    height: 390px;
    background: radial-gradient(ellipse at 40% 35%, var(--card-green) 0%, var(--card-green-deep) 100%);
    box-shadow: 0 6px 18px rgba(0,0,0,0.25);
    display: flex;
    flex-direction: column;
    align-items: center;
    color: var(--ink-teal);
  }
  .wordmark {
    font-family: "Fjalla One", sans-serif;
    font-size: 52px;
    letter-spacing: 1px;
    text-transform: uppercase;
    color: var(--ink-teal);
    line-height: 1;
  }
  /* Front */
  .card-front { justify-content: center; }
  .tagline {
    font-family: "Libre Baskerville", serif;
    font-weight: 700;
    font-size: 21px;
    color: var(--ink-black);
    margin-top: 14px;
  }
  .services {
    font-family: "Arimo", sans-serif;
    font-weight: 700;
    font-size: 16px;
    letter-spacing: 1px;
    text-transform: uppercase;
    color: var(--ink-slate);
    margin-top: 14px;
  }
  /* Back */
  .card-back { padding-top: 58px; }
  .person-name {
    font-family: "Libre Baskerville", serif;
    font-style: italic;
    font-weight: 700;
    font-size: 19px;
    text-transform: uppercase;
    color: var(--ink-black);
    margin-top: 36px;
  }
  .person-role {
    font-family: "Arimo", sans-serif;
    font-weight: 700;
    font-size: 17px;
    color: var(--ink-slate);
    margin-top: 4px;
  }
  .contact-list {
    list-style: none;
    margin-top: 40px;
    font-family: "Arimo", sans-serif;
    font-size: 18px;
    color: var(--ink-black);
    line-height: 1.5;
    text-align: left;
  }
  .contact-label {
    font-weight: 700;
    font-style: italic;
    color: var(--ink-slate);
  }
</style>
</head>
<body>
<main class="canvas">
  <section class="card card-front" aria-label="Card front">
    <h1 class="wordmark">Bramwell Pantry</h1>
    <p class="tagline">Where Good Health Meets Real Life</p>
    <p class="services">Monthly cooking classes and field trips</p>
  </section>

  <section class="card card-back" aria-label="Card back">
    <h2 class="wordmark">Bramwell Pantry</h2>
    <p class="person-name">Harriet Dunmore</p>
    <p class="person-role">Health Coach</p>
    <ul class="contact-list">
      <li><span class="contact-label">Telephone:</span> (555) 218-4476</li>
      <li><span class="contact-label">Email:</span> harriet@bramwellpantry-example.com</li>
      <li><span class="contact-label">Website:</span> www.bramwellpantry-example.com</li>
    </ul>
  </section>
</main>
</body>
</html>
```